KTLR Unique Letterhead for Financial Services Business

I am looking for a letterhead design to match our branding colours. I do not want to see anything generic that could be created in word, I can do that myself, I am after something with a bit of designer flair. Once completed I will need files in a print ready format (including bleed area).

I have included our logo file and also our new business card design but get creative.

Industry/Entity Type

Financial Services

Font styles to use
Other font styles liked:
• raleway

Colors
00AB8E
00BBA5
67D7C9
C6EFE9
E9F9F6

Requirements
Must have
• Must be consisten with logo branding colours.
Should not have
• Anything generic that I could create myself in word

```html
<!DOCTYPE html>
<html lang="en">
<head>
<meta charset="utf-8">
<title>KTLR Financial Services – Letterhead</title>
<link rel="stylesheet" href="https://fonts.googleapis.com/css2?family=Raleway:wght@500&family=Montserrat:wght@400;700&family=Questrial&family=Roboto:wght@400&family=Open+Sans:wght@600&display=swap">
<style>
  :root {
    --page-bg: #d9dadc;
    --paper: #efefef;
    --teal: #1a7f84;
    --teal-bright: #00bba5;
    --teal-brand: #00ab8e;
    --teal-deep: #00786c;
    --ink: #4a4a4a;
    --ink-soft: #5c5c5c;
    --white: #ffffff;
  }
  * { box-sizing: border-box; margin: 0; padding: 0; }
  html, body {
    width: 1119px; height: 1200px; overflow: hidden;
    background: var(--page-bg);
  }
  .letterhead {
    position: absolute; left: 141px; top: 30px;
    width: 836px; height: 1140px;
    background: var(--paper);
    box-shadow: 0 10px 30px rgba(0,0,0,.25);
    overflow: hidden;
    color: var(--ink);
  }
  .brand {
    position: absolute; left: 37px; top: 72px;
    display: flex; align-items: center; gap: 10px;
  }
  .brand-dot {
    width: 34px; height: 34px; border-radius: 50%; background: var(--teal); flex: none;
  }
  .brand-name {
    font-family: "Raleway", sans-serif; font-weight: 500;
    font-size: 22px; line-height: 1; color: var(--teal);
  }
  .contact-list {
    position: absolute; right: 45px; top: 68px; list-style: none;
    font-family: "Roboto", sans-serif; font-size: 13px; color: #2e2e2e;
  }
  .contact-list li {
    display: flex; align-items: center; justify-content: flex-end;
    gap: 6px; height: 24.5px;
  }
  .contact-icon { width: 16px; height: 16px; }
  .header-rule {
    position: absolute; left: 33px; top: 150px; width: 760px; height: 1px;
    background: linear-gradient(90deg, var(--teal-brand), var(--teal-deep));
  }
  .recipient {
    position: absolute; left: 38px; top: 270px;
    font-family: "Montserrat", sans-serif; color: var(--ink-soft);
  }
  .recipient-name {
    font-weight: 700; font-size: 27px; letter-spacing: .5px;
    color: var(--teal); margin-bottom: 10px;
  }
  .recipient p { font-size: 14.5px; line-height: 26px; }
  .recipient .address { line-height: 20px; margin-top: 3px; }
  .letter-date {
    position: absolute; right: 37px; top: 373px;
    font-family: "Open Sans", sans-serif; font-weight: 600; font-size: 17px; color: var(--ink-soft);
  }
  .letter-body {
    position: absolute; left: 33px; top: 431px; width: 766px;
    font-family: "Questrial", sans-serif; font-size: 16.4px; line-height: 18.7px;
    text-align: justify; hyphens: auto; color: #555;
  }
  .letter-body p.gap { margin-top: 18px; }
  .letter-body p.gap-lg { margin-top: 40px; }
  .sign-off {
    position: absolute; left: 580px; top: 822px;
    font-family: "Questrial", sans-serif; font-size: 21px; color: var(--ink-soft);
  }
  .signature {
    position: absolute; left: 598px; top: 868px; width: 158px; height: 95px;
    background: linear-gradient(135deg, #e4e4e4, #d8d8d8);
    border-radius: 4px;
  }
  .footer-wave { position: absolute; left: 0; bottom: 0; width: 836px; height: 140px; }
  .footer-address {
    position: absolute; left: 40px; top: 1057px;
    display: flex; gap: 8px; color: var(--white);
    font-family: "Montserrat", sans-serif; font-style: normal;
    font-size: 16px; line-height: 23px;
  }
  .footer-address svg { width: 16px; height: 22px; flex: none; }
</style>
</head>
<body>
<main class="letterhead">
  <header>
    <div class="brand">
      <span class="brand-dot"></span>
      <span class="brand-name">KTLR Financial Services</span>
    </div>
    <ul class="contact-list">
      <li>0400 182 730
        <svg class="contact-icon" viewBox="0 0 16 16"><circle cx="8" cy="8" r="8" fill="#1a7f84"/><path d="M5.3 4.2l1.4 1.6-.7 1a5 5 0 0 0 2.9 2.9l1-.7 1.6 1.4-.8 1.2C7.8 11.4 4.7 8.3 4.1 5z" fill="#fff"/></svg>
      </li>
      <li>info@ktlrfinancial.com.au
        <svg class="contact-icon" viewBox="0 0 16 16"><circle cx="8" cy="8" r="8" fill="#1a7f84"/><rect x="4" y="5.3" width="8" height="5.6" rx=".8" fill="#fff"/><path d="M4.3 5.7 8 8.6l3.7-2.9" stroke="#1a7f84" stroke-width="1" fill="none"/></svg>
      </li>
      <li>www.ktlrfinancial.com.au
        <svg class="contact-icon" viewBox="0 0 16 16"><circle cx="8" cy="8" r="8" fill="#1a7f84"/><g stroke="#fff" stroke-width=".9" fill="none"><circle cx="8" cy="8" r="4.6"/><ellipse cx="8" cy="8" rx="2" ry="4.6"/><path d="M3.4 8h9.2M4 5.8h8M4 10.2h8"/></g></svg>
      </li>
    </ul>
    <div class="header-rule"></div>
  </header>

  <section class="recipient">
    <h1 class="recipient-name">JONE SMITH</h1>
    <p>0123-456-789</p>
    <p>info@youremailaddress.com</p>
    <p class="address">1234 City Your Ln. Suite<br>123 Dallas, TX 0000</p>
  </section>
  <time class="letter-date">12 December, 2023</time>

  <article class="letter-body">
    <p>Lorem ipsum dolor sit amet, consectetuer adipiscing elit, sed diam nonummy nibh euismod tincidunt ut laoreet dolore magna aliquam erat volutpat. Ut wisi enim ad minim veniam, quis nostrud exerci tation ullamcorper suscipit lobortis nisl ut aliquip ex ea commodo consequat. Duis autem vel eum iriure dolor in hendrerit in vulputate velit esse molestie consequat, vel illum dolore eu feugiat nulla facilisis at vero eros et accumsan et iusto odio dignissim qui blandit praesent luptatum zzril delenit augue duis dolore te feugait nulla facilisi.</p>
    <p class="gap">Lorem ipsum dolor sit amet, cons ectetuer adipiscing elit, sed diam nonummy nibh euismod tincidunt ut laoreet dolore magna aliquam erat volutpat. Ut wisi enim ad minim veniam, quis nostrud exerci tation ullamcorper suscipit lobortis nisl ut aliquip ex ea commodo consequat.</p>
    <p>Lorem ipsum dolor sit amet, consectetuer adipiscing elit, sed diam nonummy nibh euismod tincidunt ut laoreet dolore magna aliquam erat</p>
    <p class="gap-lg">Lorem ipsum dolor sit amet, cons ectetuer adipiscing elit, sed diam nonummy nibh euismod tincidunt ut laoreet dolore magna aliquam erat volutpat. Ut wisi enim ad minim veniam, quis nostrud exerci tation ullamcorper suscipit lobortis nisl ut aliquip ex ea commodo consequat. Lorem ipsum dolor sit zamet, consectetuer adipiscing elit, sed diam nonummy nibh euismod tincidunt.</p>
  </article>

  <div class="sign-off">Managing Director</div>
  <div class="signature" role="img" aria-label="Handwritten signature of the managing director"></div>

  <svg class="footer-wave" viewBox="0 1000 836 140" preserveAspectRatio="none">
    <defs>
      <linearGradient id="footerTeal" x1="0" x2="1" y1="0" y2="0">
        <stop offset="0" stop-color="#00bba5"/>
        <stop offset=".5" stop-color="#00ab8e"/>
        <stop offset="1" stop-color="#00786c"/>
      </linearGradient>
      <linearGradient id="footerSwoosh" x1="0" x2="1">
        <stop offset="0" stop-color="#e4e4e4"/>
        <stop offset="1" stop-color="#9c9ea4"/>
      </linearGradient>
    </defs>
    <path d="M400 1043 C520 1075 640 1090 720 1085 C780 1082 815 1073 836 1066 L836 1076 C780 1088 700 1097 620 1092 C540 1084 460 1064 400 1043Z" fill="url(#footerSwoosh)"/>
    <path d="M0 1040 C60 1020 160 1010 260 1020 C420 1036 560 1102 700 1102 C760 1102 810 1094 836 1087 L836 1140 L0 1140Z" fill="url(#footerTeal)"/>
  </svg>
  <address class="footer-address">
    <svg viewBox="0 0 16 22"><path d="M8 1a6 6 0 0 0-6 6c0 4.5 6 10 6 10s6-5.5 6-10a6 6 0 0 0-6-6z" fill="none" stroke="#fff" stroke-width="1.8"/><circle cx="8" cy="7" r="2.2" fill="#fff"/><path d="M2 20h12" stroke="#fff" stroke-width="1.8"/></svg>
    <span>PO Box 1180 Ridgeview<br>NSW 2999</span>
  </address>
</main>
</body>
</html>
```